www.brevatin.com Sales/Order Page ReDesign

We need a new and amazing design for our sales/order page to attract more costumers and new houses for our portal.

Here is the existing page with the current design: https://www.brevatin.com/sales

We are proud owners of www.sommarhytta.no and www.brevatin.com and we want more holiday home owners to join our page so that we can rent out their holiday homes and increase the number of houses on our portal.

To get more homeowners we need a sales page that can sell our products the best way possible. Therefore we want you too blow us away with a fresh, modern, easy understandable and stylish new sales/order page.

The only restrictions we give when it comes to design is that it needs to fit the existing design of our portals, the top and footer are set. Beside that we are open for everything as long as it at once give the customers impression that this is a good, professional page were they just have to put out their houses.

When it comes to content I have added two documents who include the content to put in here and some guidelines on how to organize the page. Please be creative and add necessary graphics, symbols, background pictures and what ever necessary to make this page look professional and appealing to new costumers.

Looking forward to what suggestions we are given.

We just want to inform that we have updated our brief with a much more concrete description of what content to add on the sale page, and who to structure the content on the page. Hope this helps to make suggestions easier. Looking forward to receive some good contributions.

We would just like to make sure that everyone have understood that we are not asking for a new design suggestion to our portal in general. We are only asking for a redesign of our sales/order page you find here www.brevatin.com/sales. We have to day received some designs for our front page and the design it self was good, but that's not what we are asking for this time and don't want you to use time of something we don't need at the moment. We are looking forward too se some good suggestions.

Reason: Hello. Thanks for all the great contributions we have been given so fare. We haven't been able to respond to all design and are therefore extending the deadline so that we are able to respond to the designs we have been giver and to gov time to make final changes.

Reason: We are extending the deadline to give designers time to give new suggestion based on our latest feedback today.

Reason: Extended so we can receive last design changes.

Target Market(s)

This is a presentation page where we present our product agains new home owner who we what to choose listing there property on or site.

Industry/Entity Type

Sales

Requirements
Must have
• A modern design who calms the costumer down and help them in deciding to chose us, and for them to choose us they need to trust and believe in us. Therefore your main task is to create a page that effectively informs about our product, gets the visitors attentions and make them trust us.
Nice to have
• Examples of good competitors and good order pages we like:

http://www.cabinquest.example/info/lyp?icid=IL___O_Text___top_nav_link
https://www.nestlodge.example/rooms/new
https://www.pearvix.example/phone/compare/
http://www.guestnook.example/host
Should not have
• - Bad design :-). With bad design we mean design that looks like it's made in 2 seconds by a little child.

```html
<!DOCTYPE html>
<html lang="en">
<head>
<meta charset="utf-8">
<title>Brevatin – Flexible Advertising</title>
<link href="https://fonts.googleapis.com/css2?family=Lobster&family=Roboto:wght@300;400;500;700&display=swap" rel="stylesheet">
<style>
:root{
  --blue:#1d8fd6;
  --blue-light:#3aa6e6;
  --teal:#2cbfa8;
  --teal-2:#45c3c9;
  --mint:#6fd8b4;
  --lime:#b3d65a;
  --green-btn:#9fd049;
  --dark:#3a3a3a;
  --text:#333;
  --grey-bg:#ececec;
  --row-alt:#f1f1f1;
  --badge:#c9d3dc;
  --white:#fff;
}
*{box-sizing:border-box;margin:0;padding:0}
html,body{width:1200px;height:2609px;overflow:hidden}
body{font-family:'Roboto',sans-serif;color:var(--text);background:var(--white);position:relative}
.abs{position:absolute}

/* hero */
.hero{position:absolute;left:0;top:0;width:1200px;height:1200px;
  background:radial-gradient(ellipse at 20% 30%,#3aa88a 0%,rgba(58,168,138,0) 45%),
  radial-gradient(ellipse at 85% 15%,#cfe7f2 0%,rgba(207,231,242,0) 50%),
  radial-gradient(ellipse at 70% 55%,#8fd1b5 0%,rgba(143,209,181,0) 45%),
  linear-gradient(180deg,#a9d6e6 0%,#7ec3b2 35%,#c8e4d6 70%,#ffffff 100%)}
.topbar{position:absolute;right:0;top:0;height:28px;display:flex;align-items:center;gap:10px;padding-right:270px;font-size:12px;color:#fff}
.flag{width:20px;height:13px;display:inline-block}
.signin{background:var(--green-btn);color:#234;padding:4px 18px;font-size:11px}
.brand-tab{position:absolute;left:300px;top:0;width:180px;height:96px;background:#fff;box-shadow:0 2px 6px rgba(0,0,0,.15);
  display:flex;align-items:center;justify-content:center;gap:10px;border-bottom:8px solid var(--blue)}
.brand-tab .mark{width:26px;height:26px;background:var(--blue)}
.brand-tab .name{font-size:26px;font-weight:500;color:var(--blue)}
.hero-title{position:absolute;left:0;width:1200px;text-align:center;color:#fff}
.hero-title .script{top:128px;font-family:'Lobster',cursive;font-size:44px}
.hero-title .caps{top:172px;font-size:30px;letter-spacing:8px;font-weight:300}
.hero-rule{position:absolute;top:165px;height:1px;background:rgba(255,255,255,.7);width:120px}

/* plan cards */
.plan{position:absolute;top:238px;width:296px;height:907px;background:#fff;box-shadow:0 3px 10px rgba(0,0,0,.18);display:flex;flex-direction:column}
.plan-head{height:227px;position:relative;color:#fff;text-align:center}
.plan-free .plan-head{background:linear-gradient(160deg,var(--teal) 0%,var(--teal-2) 100%)}
.plan-year .plan-head{background:linear-gradient(160deg,#3cc9a6 0%,var(--mint) 60%,#a8e6c8 100%)}
.plan-label{display:inline-block;margin-top:32px;border:2px solid #fff;padding:9px 14px;font-size:15px;letter-spacing:1px}
.plan-price{font-size:34px;font-weight:300;margin-top:34px}
.plan-old{font-size:18px;text-decoration:line-through;margin-top:12px}
.plan-year .plan-price{margin-top:0}
.offer{position:absolute;left:0;bottom:0;width:100%;height:40px;background:var(--lime);color:#233;font-size:24px;line-height:40px}
.details-bar{height:26px;background:var(--dark);color:#fff;text-align:center;font-size:20px;line-height:26px;font-weight:300}
.row{text-align:center;padding:0 22px;display:flex;flex-direction:column;justify-content:center;font-size:12px;line-height:1.4}
.row:nth-child(even){background:var(--row-alt)}
.row h3{font-size:15px;font-weight:400;letter-spacing:.5px;margin-bottom:10px;color:#222}
.row h3.accent{color:var(--blue-light)}
.listing-badge{display:block;width:110px;height:32px;margin:10px auto;background:var(--badge);border-radius:4px}
.price-table{width:100%;font-size:12px;border-collapse:collapse;text-align:left;margin-top:8px}
.price-table td{padding:3px 0;border-bottom:1px solid #ddd}
.price-table s{color:#777}

/* features */
.features{position:absolute;left:320px;top:1230px;width:600px}
.feature{display:flex;gap:14px;margin-bottom:30px}
.feature .ic{flex:0 0 36px;height:36px}
.feature h4{color:var(--blue-light);font-weight:400;font-size:15px;letter-spacing:1px}
.feature p{font-size:13px;line-height:1.35;color:#333}

/* grey order area */
.order{position:absolute;left:0;top:1580px;width:1200px;height:855px;background:var(--grey-bg)}
.sec-title{position:absolute;left:300px;font-family:'Lobster',cursive;font-size:24px;color:#333;font-weight:400}
.sec-rule{position:absolute;left:300px;width:605px;height:1px;background:#cfcfcf}
.prod{position:absolute;top:1647px;width:196px;height:157px;background:#fff;box-shadow:0 1px 3px rgba(0,0,0,.15);text-align:center;display:flex;flex-direction:column}
.prod .lbl{color:var(--blue-light);font-size:12px;letter-spacing:.5px;height:58px;display:flex;align-items:center;justify-content:center;line-height:1.3;padding:0 8px}
.prod .val{font-size:34px;color:var(--blue-light);font-weight:300;flex:1;display:flex;align-items:center;justify-content:center;border-top:1px solid #e0e0e0}
.prod .add{height:38px;background:var(--green-btn);display:flex;align-items:center;justify-content:center;gap:10px;font-size:17px}
.box{width:20px;height:20px;background:#fff;border:1px solid #bbb;display:inline-block}
.total{position:absolute;left:720px;top:1842px;font-size:16px;letter-spacing:1px}
.total b{color:var(--blue-light);font-size:24px;font-weight:400}
.form-label{position:absolute;left:307px;font-size:11px;letter-spacing:.5px}
.input{position:absolute;height:20px;background:#fff;border:1px solid #ddd;font-size:10px;padding-left:6px;line-height:18px}
.terms{position:absolute;left:305px;top:2318px;width:360px;font-size:8px;line-height:1.55;color:#555}
.confirm{position:absolute;left:687px;top:2367px;width:215px;height:40px;background:var(--lime);color:#233;font-size:18px;letter-spacing:1px;text-align:center;line-height:40px;box-shadow:0 1px 2px rgba(0,0,0,.25)}

/* footer */
.footer{position:absolute;left:0;top:2435px;width:1200px;height:174px;background:var(--blue);color:#fff;font-size:10px}
.fcol{position:absolute;top:22px;line-height:1.55}
.fcol h5{font-size:11px;font-weight:500;margin-bottom:3px}
.fcol li{list-style:none;display:flex;align-items:center;gap:5px}
.fcol li::before{content:"";width:8px;height:8px;border-radius:50%;background:#fff}
.map{position:absolute;left:420px;top:36px;width:115px;height:62px;background:linear-gradient(135deg,rgba(255,255,255,.85),rgba(255,255,255,.6));border-radius:26px 10px 34px 18px}
</style>
</head>
<body>

<section class="hero" role="img" aria-label="Blurred holiday landscape of sky, water and greenery"></section>
<div class="topbar">
  <span class="flag" style="background:#c8102e"></span>
  <span class="flag" style="background:#1f3f8f"></span>
  <span class="signin">Sign in</span>
  <span>List your property</span>
</div>
<div class="brand-tab"><span class="mark"></span><span class="name">Brevatin</span></div>

<div class="hero-title"><div class="abs script" style="width:1200px">Flexible</div></div>
<div class="hero-rule" style="left:410px"></div>
<div class="hero-rule" style="left:670px"></div>
<div class="hero-title"><div class="abs caps" style="width:1200px">ADVERTISING</div></div>

<article class="plan plan-free" style="left:300px">
  <div class="plan-head">
    <div class="plan-label">FREE ADVERTISING</div>
    <div class="plan-price">NOK 0,-</div>
  </div>
  <div class="details-bar">Details</div>
  <div class="rows">
    <div class="row" style="height:100px"><h3>NO LISTING FEE</h3><p>No fixed fee for advertising.</p></div>
    <div class="row" style="height:110px"><h3>RUNNING COSTS</h3><p>Pay a provision, just 18% on the booking you receive. A transaction fee of 4.5% will be added.</p></div>
    <div class="row" style="height:90px"><h3>YOU SELECT PERIOD</h3><p>You can advertise as long as you wish.</p></div>
    <div class="row" style="height:100px"><h3 class="accent">UNLIMITED NUMBER OF IMAGES</h3><p>Upload an unlimited number of images of your property.</p></div>
    <div class="row" style="height:254px;justify-content:flex-start;padding-top:22px">
      <h3>BROAD MARKETING</h3><p>Optional listing at</p>
      <span class="listing-badge" role="img" aria-label="Listing partner badge"></span>
      <table class="price-table">
        <tr><td>60 days</td><td>400 NOK</td><td></td></tr>
        <tr><td>120 days</td><td>700 NOK</td><td></td></tr>
        <tr><td>240 days</td><td>1 300 NOK</td><td></td></tr>
        <tr><td>1 year</td><td><s>1 900 NOK</s></td><td>700 NOK</td></tr>
      </table>
    </div>
  </div>
</article>

<article class="plan plan-year" style="left:608px">
  <div class="plan-head">
    <div class="plan-label">YEARLY ADVERTISING</div>
    <div class="plan-old">NOK 7990,-</div>
    <div class="plan-price">NOK 4990,-</div>
    <div class="offer">Special offer &nbsp;38% off</div>
  </div>
  <div class="details-bar">Details</div>
  <div class="rows">
    <div class="row" style="height:100px"><h3>ONE YEARLY FIXED PRICE</h3><p>Pay a fixed yearly price for advertising. No limits on number of bookings.</p></div>
    <div class="row" style="height:110px"><h3>RUNNING COSTS</h3><p>No provision. There is a transaction fee on 4.5%</p></div>
    <div class="row" style="height:90px"><h3>ADVERTISING FOR 12 MONTHS</h3><p>You are guaranteed advertising for 12 months, from the publishing date.</p></div>
    <div class="row" style="height:100px"><h3>UNLIMITED NUMBER OF IMAGES</h3><p>Upload an unlimited number of images of your property.</p></div>
    <div class="row" style="height:254px"><h3>BROAD MARKETING</h3><p>Listing included at</p>
      <span class="listing-badge" role="img" aria-label="Listing partner badge"></span></div>
  </div>
</article>

<section class="features">
  <div class="feature"><svg class="ic" viewBox="0 0 36 36"><circle cx="18" cy="18" r="16" fill="none" stroke="#3aa6e6" stroke-width="2"/><path d="M18 10v16M10 18h16" stroke="#3aa6e6" stroke-width="3"/></svg>
    <div><h4>YOUR OWN HOUSING ADVISOR</h4><p>We are concerned with your rental and advertising. You are assigned your personal advisor, which can advice and give recommendations to make your listing more attractive.</p></div></div>
  <div class="feature"><svg class="ic" viewBox="0 0 36 36"><circle cx="18" cy="18" r="16" fill="none" stroke="#3aa6e6" stroke-width="2"/><path d="M18 10v16M10 18h16" stroke="#3aa6e6" stroke-width="3"/></svg>
    <div><h4>RELAX AND WAIT FOR BOOKINGS</h4><p>Our call center is ready to assist your guests before, during and after the stay. You can use your time on important things, we'll take care of payments and administering your bookings.</p></div></div>
  <div class="feature"><svg class="ic" viewBox="0 0 36 36"><circle cx="18" cy="18" r="16" fill="none" stroke="#3aa6e6" stroke-width="2"/><path d="M18 10v16M10 18h16" stroke="#3aa6e6" stroke-width="3"/></svg>
    <div><h4>ONLINE BOOKING</h4><p>Your property will be available for booking 24 hours a day, 7 days a week, 365 days a year.</p></div></div>
  <div class="feature"><svg class="ic" viewBox="0 0 36 36"><circle cx="18" cy="18" r="16" fill="none" stroke="#3aa6e6" stroke-width="2"/><path d="M18 10v16M10 18h16" stroke="#3aa6e6" stroke-width="3"/></svg>
    <div><h4>ONLINE CALENDAR</h4><p>Your property will have an online calendar which is automatically maintained.</p></div></div>
</section>

<section class="order"></section>
<h2 class="sec-title" style="top:1596px">Properties</h2>
<div class="sec-rule" style="top:1634px"></div>
<div class="prod" style="left:300px"><div class="lbl">COMMISSIONS<br>BASED ADVERTISING</div><div class="val">0,-</div><div class="add">Add <span class="box"></span></div></div>
<div class="prod" style="left:504px"><div class="lbl">COMMISSIONS<br>BASED ADVERTISING<br>and listing at Listra.no - 1 year</div><div class="val">700,-</div><div class="add">Add <span class="box"></span></div></div>
<div class="prod" style="left:708px"><div class="lbl">YEARLY ADVERTISING<br>Includes listing at Listra.no</div><div class="val">4990,-</div><div class="add">Add <svg width="20" height="20" viewBox="0 0 20 20"><rect x=".5" y=".5" width="19" height="19" fill="#fff" stroke="#bbb"/><path d="M4 10l4 5 9-12" stroke="#3aa6e6" stroke-width="3" fill="none"/></svg></div></div>
<div class="total">TOTAL : <b>4990,-</b></div>

<h2 class="sec-title" style="top:1918px">Customer details</h2>
<div class="sec-rule" style="top:1956px"></div>
<span class="form-label" style="top:1978px">CUSTOMER TYPE</span><div class="input" style="left:432px;top:1975px;width:290px">PRIVATE CUSTOMER ▾</div>
<span class="form-label" style="top:2011px">FIRSTNAME</span><div class="input" style="left:432px;top:2008px;width:200px"></div>
<span class="form-label" style="top:2044px">LASTNAME</span><div class="input" style="left:432px;top:2041px;width:200px"></div>
<span class="form-label" style="top:2077px">ADDRESS</span><div class="input" style="left:432px;top:2074px;width:470px"></div>
<span class="form-label" style="top:2110px">POSTNO / PLACE</span><div class="input" style="left:432px;top:2107px;width:90px"></div><div class="input" style="left:530px;top:2107px;width:150px"></div>
<span class="form-label" style="top:2143px">E-MAIL</span><div class="input" style="left:432px;top:2140px;width:200px"></div>
<span class="form-label" style="top:2176px">CONFIRM E-MAIL</span><div class="input" style="left:432px;top:2173px;width:200px"></div>
<span class="form-label" style="top:2209px">PHONE</span><div class="input" style="left:432px;top:2206px;width:70px">+ 47 ▾</div><div class="input" style="left:510px;top:2206px;width:180px"></div>

<h2 class="sec-title" style="top:2268px">Terms</h2>
<div class="sec-rule" style="top:2306px"></div>
<div class="terms">
  <p>We in Brevatin Holiday Homes ask you to confirm the following details before ordering.</p>
  <p style="margin-top:6px">Flexible listing runs for one full year from the date of publishing.<br>The price is paid once and the listing stays active for the period.<br>Bookings are handled by our staff and paid out each month.<br>The owner can pause the listing at any time by contacting us.</p>
  <p style="margin-top:10px;display:flex;align-items:center;gap:8px;font-size:9px"><span class="box" style="width:14px;height:14px"></span>I have read, understood and agree to the terms for this order</p>
</div>
<div class="confirm">CONFIRM ORDER ›</div>

<footer class="footer">
  <div class="fcol" style="left:300px"><h5>Destinations</h5><ul><li>Europe</li><li>North America</li><li>South America</li><li>Africa</li><li>Asia</li><li>Australia</li></ul></div>
  <div class="map" role="img" aria-label="Simplified world map"></div>
  <div class="fcol" style="left:555px"><h5>For tenants</h5><ul><li>My page</li><li>Why book</li><li>FAQ</li><li>Guarantees</li></ul></div>
  <div class="fcol" style="left:665px"><h5>For house owners</h5><ul><li>My home</li><li>List on our site</li><li>Conditions</li></ul></div>
  <div class="fcol" style="left:780px"><h5>Contact us</h5>
    <div>Brevatin Holiday Homes</div><div>post@brevatin.com</div><div>+47 21 40 55 90</div><div>www.brevatin.com</div>
    <h5 style="margin-top:4px">Opening hours</h5><div>Mon - Fri: 9.00 - 17.00</div><div>Sat - Sun: Closed</div></div>
</footer>

</body>
</html>
```